Company or website name
- StepTrova
- Links to the website
- www.steptrova.com
- Describe your company and organization and target audience
- Dance Class finder website  Primary target audience : Dance enthusiasts Goal: To allow dance enthusiasts to search for dance classes and studios in their immediate area that offers the dance classes they desire at specific time and days w/o having to deal with the hassle of searching through every studio's dance schedule  Secondary target audience: Dance Instructors Goal: To allow dance instructors to network with studios, create a following of dance students, educate the public on the classes they instruct (ie. What class, when, where, etc...).  Tertiary target audience: Dance Studios Goal: To give dance studios organizational tools that will allow them to manage their business and schedule better.
- The design should have the following
- Colors: Red, grey, purple  Logo: Silhouette of dancers in movement practicing different forms of dance. Logo will be background to "StepTrova" lettering.  "StepTrova" lettering: Letters placed together without spacing or adding characters in place of letters. I would like this to "Pop"
- Other Facts

```html
<!DOCTYPE html>
<html lang="en">
<head>
<meta charset="utf-8">
<title>StepTrova – Find Dance Classes Near You</title>
<link rel="stylesheet" href="https://fonts.googleapis.com/css2?family=Montserrat:wght@800;900&family=Questrial&family=Hind:wght@400;500;600&family=Open+Sans:wght@400;600;700&display=swap">
<style>
:root{
  --purple:#7e0d7e;
  --purple-dark:#6b0a6b;
  --yellow:#f4c81e;
  --blue:#43659b;
  --ink:#222;
  --muted:#8a8a8a;
  --line:#dcdcdc;
  --footer:#f2f2f2;
  --footer-bottom:#e6e6e6;
  --white:#fff;
}
*{margin:0;padding:0;box-sizing:border-box}
html,body{width:1200px;height:2535px;overflow:hidden}
body{position:relative;background:var(--white);font-family:"Open Sans",sans-serif;color:var(--ink)}
.abs{position:absolute}

/* header */
.site-header{position:absolute;left:0;top:0;width:1200px;height:83px;background:var(--purple)}
.brand{position:absolute;left:236px;top:22px;color:var(--white);font-family:"Montserrat",sans-serif;font-weight:900;font-size:30px;letter-spacing:0}
.brand-dot{display:inline-block;width:12px;height:12px;border-radius:50%;background:var(--white);margin-right:8px;vertical-align:middle}
.contact{position:absolute;top:9px;right:233px;display:flex;gap:20px;color:var(--white);font-size:8.5px;align-items:center}
.contact span{display:flex;align-items:center;gap:4px}
.social{position:absolute;top:34px;right:234px;display:flex;gap:9px}
.social i{display:block;width:8px;height:8px;border-radius:50%;background:#c792c7}
.main-nav{position:absolute;top:62px;right:233px;display:flex;gap:17px}
.main-nav a{color:var(--white);text-decoration:none;font-size:9px;font-weight:600;letter-spacing:.2px;position:relative;padding-bottom:8px}
.main-nav a.active{color:var(--yellow)}
.main-nav a.active::after{content:"";position:absolute;left:0;right:0;bottom:0;height:3px;background:var(--yellow)}

/* hero */
.hero{position:absolute;left:0;top:83px;width:1200px;height:410px;background:linear-gradient(180deg,#f4f4f4 0%,#e3e3e3 100%);overflow:hidden}
.hero-paint{position:absolute;left:0;top:0;width:1200px;height:130px;background:linear-gradient(90deg,#39a9d9 0%,#a6d4ea 22%,#f3f3f3 40%,#f3f3f3 60%,#f3d36a 78%,#e45a3a 90%,#5bbf7a 100%);opacity:.55}
.hero-photo{position:absolute;left:560px;top:95px;width:460px;height:300px;background:radial-gradient(ellipse at center,#b8bcc4 0%,#d6d6d8 55%,rgba(228,228,228,0) 75%)}
.hero-title{position:absolute;left:234px;top:120px;font-family:"Montserrat",sans-serif;font-weight:900;font-size:37px;line-height:34px;color:var(--purple);letter-spacing:.3px}
.hero-rule{position:absolute;left:235px;top:201px;width:30px;height:3px;background:var(--white)}
.hero-sub{position:absolute;left:234px;top:218px;font-family:"Hind",sans-serif;font-size:14.5px;color:#1b1b1b}
.search{position:absolute;left:235px;top:261px;width:240px;height:32px;background:var(--white);border:1px solid #d5d5d5;display:flex;align-items:center;justify-content:space-between;padding:0 12px}
.search span{font-size:8.5px;font-weight:600;color:#333;letter-spacing:.2px}

/* section titles */
.section-title{position:absolute;left:0;width:1200px;text-align:center;font-family:"Questrial",sans-serif;font-size:24px;color:var(--purple)}
.section-rule{position:absolute;left:586px;width:29px;height:2px;background:var(--line)}

/* studio cards */
.studio{position:absolute;width:233px;height:112px;background:var(--white);border:1px solid #e3e3e3;box-shadow:0 1px 3px rgba(0,0,0,.08);display:flex}
.studio-photo{width:100px;height:100%;background:linear-gradient(135deg,#6b5a8c 0%,#3f6fb0 45%,#b6d33a 100%)}
.studio-photo.alt{background:linear-gradient(135deg,#9a8fa6 0%,#d9458f 50%,#54545c 100%)}
.studio-body{padding:15px 10px 0 11px}
.studio-body h3{font-family:"Questrial",sans-serif;font-weight:400;font-size:12.5px;color:var(--purple)}
.studio-body hr{border:0;width:20px;height:1px;background:var(--line);margin:8px 0 7px}
.studio-body p{font-family:"Hind",sans-serif;font-size:8.6px;line-height:11.7px;color:#666}

/* about */
.about-photo{position:absolute;left:0;top:947px;width:600px;height:380px;background:linear-gradient(160deg,#d7e6ea 0%,#4bb6c4 40%,#c98a5a 75%,#9a7250 100%)}
.about-panel{position:absolute;left:600px;top:947px;width:600px;height:380px;background:var(--purple)}
.about-title{position:absolute;left:35px;top:58px;font-family:"Montserrat",sans-serif;font-weight:900;font-size:33px;line-height:33px;color:var(--white)}
.about-title span{color:var(--yellow)}
.about-rule{position:absolute;left:35px;top:141px;width:29px;height:3px;background:var(--yellow)}
.about-text{position:absolute;left:35px;top:162px;width:330px;font-size:9.6px;line-height:13.1px;color:var(--white)}
.btn-outline{position:absolute;left:35px;top:285px;width:90px;height:32px;border:1px solid var(--white);color:var(--yellow);font-size:8.5px;font-weight:700;display:flex;align-items:center;justify-content:center}

/* instructors */
.instructor{position:absolute;top:1471px;width:170px;height:277px;background:var(--white);border:1px solid #e4e4e4;box-shadow:0 2px 5px rgba(0,0,0,.1)}
.instructor.featured{box-shadow:0 6px 10px rgba(0,0,0,.2)}
.avatar{position:absolute;left:18px;top:19px;width:42px;height:42px;background:linear-gradient(180deg,#6a4a36,#c79c7e)}
.avatar.light{background:linear-gradient(180deg,#c9b07c,#e8d3b7)}
.avatar.dark{background:linear-gradient(180deg,#2a2222,#8a6a58)}
.instructor h3{position:absolute;left:17px;top:74px;font-family:"Questrial",sans-serif;font-weight:400;font-size:13px;color:var(--purple)}
.instructor .rule{position:absolute;left:17px;top:102px;width:22px;height:1px;background:var(--line)}
.instructor p{position:absolute;left:17px;top:116px;width:140px;font-family:"Hind",sans-serif;font-size:9px;line-height:13.2px;color:#777}
.instructor .sep{position:absolute;left:17px;right:15px;top:237px;height:1px;background:#e6e6e6}
.instructor .more{position:absolute;left:19px;top:250px;font-family:"Hind",sans-serif;font-weight:600;font-size:10px;color:#666}
.instructor.featured .more{color:var(--purple)}

/* promo band */
.promo{position:absolute;left:0;top:1816px;width:1200px;height:391px;background:var(--blue)}
.promo-photo{position:absolute;left:300px;top:0;width:620px;height:391px;background:radial-gradient(ellipse at center,rgba(80,60,130,.55) 0%,rgba(67,101,155,0) 70%)}
.promo-kicker{position:absolute;left:0;top:99px;width:1200px;text-align:center;font-family:"Questrial",sans-serif;font-size:17px;color:var(--yellow)}
.promo-title{position:absolute;left:0;top:118px;width:1200px;text-align:center;font-family:"Montserrat",sans-serif;font-weight:900;font-size:31px;color:var(--yellow);letter-spacing:.5px}
.promo-rule{position:absolute;left:586px;top:172px;width:29px;height:3px;background:var(--white)}
.promo-text{position:absolute;left:0;top:186px;width:1200px;text-align:center;font-size:9.6px;line-height:18.3px;color:var(--white)}
.btn-solid{position:absolute;left:555px;top:264px;width:90px;height:31px;background:var(--yellow);color:#6a4a10;font-size:8.5px;font-weight:700;display:flex;align-items:center;justify-content:center}

/* footer */
.site-footer{position:absolute;left:0;top:2207px;width:1200px;height:253px;background:var(--footer)}
.footer-brand{position:absolute;left:235px;top:60px;font-family:"Montserrat",sans-serif;font-weight:900;font-size:21px;color:#333}
.footer-col{position:absolute;top:65px}
.footer-col h4{font-size:8.6px;font-weight:600;color:#333;margin-bottom:8px}
.footer-col li{list-style:none;font-family:"Hind",sans-serif;font-size:8.4px;line-height:15px;color:#888}
.footer-bottom{position:absolute;left:0;top:2460px;width:1200px;height:75px;background:var(--footer-bottom);text-align:center}
.footer-bottom .copy{margin-top:14px;font-size:7px;font-weight:600;color:#333}
.footer-bottom p{width:720px;margin:3px auto 0;font-size:6.4px;line-height:9.8px;color:#888}
</style>
</head>
<body>

<header class="site-header">
  <div class="brand"><span class="brand-dot"></span>StepTrova</div>
  <div class="contact">
    <span><svg width="9" height="9" viewBox="0 0 24 24"><path fill="#fff" d="M6.6 10.8a15 15 0 0 0 6.6 6.6l2.2-2.2c.3-.3.7-.4 1-.2 1.1.4 2.3.6 3.6.6.6 0 1 .4 1 1V20c0 .6-.4 1-1 1A17 17 0 0 1 3 4c0-.6.4-1 1-1h3.5c.6 0 1 .4 1 1 0 1.3.2 2.5.6 3.6.1.3 0 .7-.2 1z"/></svg>(555) 210-4830</span>
    <span><svg width="10" height="10" viewBox="0 0 24 24"><circle cx="12" cy="12" r="10" fill="none" stroke="#fff" stroke-width="2"/><path d="M2 12h20M12 2c3 3 3 17 0 20M12 2c-3 3-3 17 0 20" fill="none" stroke="#fff" stroke-width="1.5"/></svg>español</span>
  </div>
  <div class="social"><i></i><i></i><i></i><i></i><i></i></div>
  <nav class="main-nav">
    <a class="active">HOME</a><a>ABOUT US</a><a>NEWS</a><a>DANCE CLASSES</a><a>DANCE INSTRUCTORS</a><a>DANCE STUDIOS</a>
  </nav>
</header>

<section class="hero">
  <div class="hero-paint" role="img" aria-label="Splashes of coloured paint smoke across the top of the banner"></div>
  <div class="hero-photo" role="img" aria-label="Two street dancers leaping together mid-move"></div>
  <h1 class="hero-title">LOREM IPSUM DOLOR<br>CONSECTETUR</h1>
  <div class="hero-rule"></div>
  <p class="hero-sub">Cras vel libero ut lacus eleifend tempor. Phasellus eleifend</p>
  <div class="search"><span>SEARCH FOR DANCE CLASSES NEAR YOU</span>
    <svg width="13" height="13" viewBox="0 0 24 24"><circle cx="10" cy="10" r="7" fill="none" stroke="#7e0d7e" stroke-width="2.5"/><path d="M15 15l6 6" stroke="#7e0d7e" stroke-width="2.5"/></svg>
  </div>
</section>

<h2 class="section-title" style="top:549px">Dance Studios</h2>
<div class="section-rule" style="top:591px"></div>

<article class="studio" style="left:234px;top:622px"><div class="studio-photo alt" role="img" aria-label="Dancers posing in a studio"></div><div class="studio-body"><h3>Lorem ipsum dolo</h3><hr><p>Lorem ipsum dolor sit ame consectetur adipiscing elit. Nulla lobortis consequat mauris, eget eleifend</p></div></article>
<article class="studio" style="left:484px;top:622px"><div class="studio-photo" role="img" aria-label="Dance class in a studio"></div><div class="studio-body"><h3>Lorem ipsum dolo</h3><hr><p>Lorem ipsum dolor sit ame consectetur adipiscing elit. Nulla lobortis consequat mauris, eget eleifend</p></div></article>
<article class="studio" style="left:734px;top:622px"><div class="studio-photo" role="img" aria-label="Dance class in a studio"></div><div class="studio-body"><h3>Lorem ipsum dolo</h3><hr><p>Lorem ipsum dolor sit ame consectetur adipiscing elit. Nulla lobortis consequat mauris, eget eleifend</p></div></article>
<article class="studio" style="left:234px;top:753px"><div class="studio-photo" role="img" aria-label="Dance class in a studio"></div><div class="studio-body"><h3>Lorem ipsum dolo</h3><hr><p>Lorem ipsum dolor sit ame consectetur adipiscing elit. Nulla lobortis consequat mauris, eget eleifend</p></div></article>
<article class="studio" style="left:484px;top:753px"><div class="studio-photo" role="img" aria-label="Dance class in a studio"></div><div class="studio-body"><h3>Lorem ipsum dolo</h3><hr><p>Lorem ipsum dolor sit ame consectetur adipiscing elit. Nulla lobortis consequat mauris, eget eleifend</p></div></article>
<article class="studio" style="left:734px;top:753px"><div class="studio-photo" role="img" aria-label="Dance class in a studio"></div><div class="studio-body"><h3>Lorem ipsum dolo</h3><hr><p>Lorem ipsum dolor sit ame consectetur adipiscing elit. Nulla lobortis consequat mauris, eget eleifend</p></div></article>

<div class="about-photo" role="img" aria-label="Group of dancers jumping in a bright studio"></div>
<section class="about-panel">
  <h2 class="about-title">ABOUT<br><span>STEPTROVA</span></h2>
  <div class="about-rule"></div>
  <p class="about-text">Lorem ipsum dolor sit amet, consectetur adipiscing elit. Nulla lobortis consequat mauris, eget eleifend nunc viverra viverra. Ut ac risus odio. Aliquam pretium purus sed nulla feugiat blandit. Cras vel libero ut lacus eleifend tempor. Phasellus eleifend, magna non tincidunt accumsan, justo arcu cursus ipsum, non porttitor sapien quam vel magna. Maecenas elit nisl, molestie nec dapibus nec, aliquet a erat. Donec scelerisque lacus a libero suscipit auctor volutpat enim euismod.</p>
  <div class="btn-outline">READ MORE</div>
</section>

<h2 class="section-title" style="top:1395px">Dance Instructors Near You</h2>
<div class="section-rule" style="top:1437px"></div>

<article class="instructor" style="left:234px"><div class="avatar" role="img" aria-label="Instructor portrait"></div><h3>Donec a lectus</h3><div class="rule"></div><p>Lorem ipsum dolor sit amet, consectetur adipiscing elit. Nulla lobortis consequat mauris, eget eleifend nunc viverra viverra. Ut ac risus odio. Aliquam pretium purus sed nulla feugiat blandit. Cras vel libero ut lacus eleifend tempor. Phasellus eleifend,</p><div class="sep"></div><div class="more">Read More</div></article>
<article class="instructor featured" style="left:422px"><div class="avatar light" role="img" aria-label="Instructor portrait"></div><h3>Donec a lectus</h3><div class="rule"></div><p>Lorem ipsum dolor sit amet, consectetur adipiscing elit. Nulla lobortis consequat mauris, eget eleifend nunc viverra viverra. Ut ac risus odio. Aliquam pretium purus sed nulla feugiat blandit. Cras vel libero ut lacus eleifend tempor. Phasellus eleifend,</p><div class="sep"></div><div class="more">Read More</div></article>
<article class="instructor" style="left:609px"><div class="avatar dark" role="img" aria-label="Instructor portrait"></div><h3>Donec a lectus</h3><div class="rule"></div><p>Lorem ipsum dolor sit amet, consectetur adipiscing elit. Nulla lobortis consequat mauris, eget eleifend nunc viverra viverra. Ut ac risus odio. Aliquam pretium purus sed nulla feugiat blandit. Cras vel libero ut lacus eleifend tempor. Phasellus eleifend,</p><div class="sep"></div><div class="more">Read More</div></article>
<article class="instructor" style="left:797px"><div class="avatar light" role="img" aria-label="Instructor portrait"></div><h3>Donec a lectus</h3><div class="rule"></div><p>Lorem ipsum dolor sit amet, consectetur adipiscing elit. Nulla lobortis consequat mauris, eget eleifend nunc viverra viverra. Ut ac risus odio. Aliquam pretium purus sed nulla feugiat blandit. Cras vel libero ut lacus eleifend tempor. Phasellus eleifend,</p><div class="sep"></div><div class="more">Read More</div></article>

<section class="promo">
  <div class="promo-photo" role="img" aria-label="Street dancers in motion tinted blue"></div>
  <p class="promo-kicker">Lorem ipsum dolor sit amet</p>
  <h2 class="promo-title">CONSECTETUR ADIPISCING ELIT</h2>
  <div class="promo-rule"></div>
  <p class="promo-text">Lorem ipsum dolor sit amet, consectetur adipiscing elit. Nulla lobortis consequat mauris,<br>eget eleifend nunc viverra viverra. Ut ac risus odio. Lorem ipsum dolor sit amet, consectetur adipiscing elit. Nulla lobortis consequat<br>mauris, eget eleifend nunc viverra viverra. Ut ac risus odio.</p>
  <div class="btn-solid">READ MORE</div>
</section>

<footer class="site-footer">
  <div class="footer-brand">StepTrova</div>
  <div class="footer-col" style="left:396px"><h4>LOREM IPSUM</h4><ul><li>Lorem ipsum dolor</li><li>Sit amet consectetur</li><li>Adipiscing elit</li><li>Nulla lobortis consequat</li><li>Mauris eget eleifend</li><li>Nunc viverra viverra</li><li>Ut ac risus odio</li></ul></div>
  <div class="footer-col" style="left:527px"><h4>EGET PULVINAR</h4><ul><li>Lorem ipsum</li><li>Dolor sit amet</li><li>Consectetur adipis</li><li>Cing elit Nulla lobortis</li><li>Consequat mauris</li></ul></div>
  <div class="footer-col" style="left:651px"><h4>DONEC PORTTITOR</h4><ul><li>Lorem ipsum dolor</li><li>Sit amet consectetur</li><li>Adipiscing elit</li><li>Nulla lobortis</li><li>Consequat Mauris</li><li>Eget eleifend</li><li>Nunc viverra viverra</li><li>Ut ac risus odio</li><li>Aliquam pretium purus</li></ul></div>
  <div class="footer-col" style="left:777px"><h4>NULLA FEUGIAT</h4><ul><li>Lorem ipsum</li><li>Dolor Sit</li><li>Amet consectetur</li><li>Adipiscing elit</li></ul></div>
  <div class="footer-col" style="left:893px"><h4>PULVINAR</h4><ul><li>Lorem</li><li>Ipsum dolor</li><li>Sit amet</li><li>Consectetur Adipis</li><li>Cing elit</li><li>Nulla lobortis</li><li>Consequat Mauris</li><li>Eget eleifend</li></ul></div>
</footer>
<div class="footer-bottom">
  <div class="copy">Copyright 2017 StepTrova</div>
  <p>Find dance classes, studios and instructors near you in one simple search. Compare schedules by day and time, follow the teachers you love, and book a spot without digging through every studio calendar. Studios manage classes, rooms and bookings with tools built for busy teams. Instructors share where and when they teach and build a following of students. Join a growing community of dancers, teachers and studios who move together every week across the city and beyond.</p>
</div>

</body>
</html>
```